Create Brisk Lesson Studio a card design that will stick in the mind of prospects.

Brisk Lesson Studio specialises designs and produces training video, animation, illustration and text.

We need a card design that oozes class and leaves the prospect brimming with confidence.

The design will feature the Brisk Lesson Studio all black logo (uploaded). The design may also use the shade of orange from the orange version of the logo (uploaded). Note, just the color is to be used e.g. for the back of the card, not the orange logo itself.

The Brisk brand is about authenticity, quality, maturity and assurance. We are a safe buy when it comes to the prospects next project.

Target Market(s)

The primary target is training managers or others who are responsible for choosing to hire companies to produce their training media e.g. video. This will usually be a large spend so they need to have confidence.

Industry/Entity Type

Training

Contact Information for Business Card

FRONT:

Brisk Lesson Studio
Phone: 03 5172 4039
1st Floor, 418 Kellerby Road
Mt Ferncombe
VIC 3862
Australia
www.brisklesson.com.au

Lionel Petch
Founder and Lead Consultant
mobile: +61 3 0462 735 218
email: lionel@brisklesson.com.au

BACK:
Specialising in design and production of training:

video
animation
illustration
text

for delivery via internet, intranet and/or LMS.

Number of Pages Required

4 page

Font styles to use
Sans Serif

Requirements
Must have
• The black logo uploaded with the brief.
Nice to have
• The inclusion of the shade of orange found in the orange logo also uploaded with the brief. One example would be having the back of the card in this orange and using a white font for the text. But I want the designer to work this out.
Should not have
• No colours other than black and the orange included in the uploaded orange logo.

```html
<!DOCTYPE html>
<html lang="en">
<head>
<meta charset="utf-8">
<title>Brisk Lesson Studio – Business Card</title>
<link rel="stylesheet" href="https://fonts.googleapis.com/css2?family=Open+Sans:wght@400;600&display=swap">
<style>
  :root {
    --backdrop: #3a3a3b;
    --card: #1b1b1c;
    --orange: #f15a22;
    --text-grey: #b4b4b4;
    --rule-grey: #5a5a5a;
  }
  * { box-sizing: border-box; margin: 0; padding: 0; }
  html, body {
    width: 1200px;
    height: 1189px;
    overflow: hidden;
    background: var(--backdrop);
    font-family: "Open Sans", Verdana, sans-serif;
  }
  .canvas {
    position: relative;
    width: 1200px;
    height: 1189px;
  }
  .card {
    position: absolute;
    left: 160px;
    width: 880px;
    height: 500px;
    background: var(--card);
    border-radius: 26px;
    box-shadow: 0 10px 30px rgba(0,0,0,0.45);
  }
  .card--back { top: 70px; }
  .card--front { top: 620px; }

  /* Brand mark: name with a plain circle */
  .brand {
    position: absolute;
    display: flex;
    align-items: center;
    justify-content: center;
    border: 3px solid var(--orange);
    border-radius: 50%;
  }
  .brand__name {
    font-weight: 600;
    color: var(--orange);
    letter-spacing: 1px;
  }
  .card--back .brand {
    left: 340px; top: 60px;
    width: 200px; height: 200px;
  }
  .card--back .brand__name { font-size: 54px; }

  .tagline {
    position: absolute;
    left: 0; right: 0; top: 310px;
    text-align: center;
    color: var(--text-grey);
    font-size: 25px;
    line-height: 38px;
  }

  .card--front .brand {
    left: 90px; top: 120px;
    width: 260px; height: 260px;
  }
  .card--front .brand__name { font-size: 70px; }

  .divider {
    position: absolute;
    left: 430px; top: 100px;
    width: 1px; height: 330px;
    background: var(--rule-grey);
  }

  .contact {
    position: absolute;
    left: 460px; top: 82px;
    width: 390px;
    color: var(--text-grey);
    font-size: 19px;
    line-height: 27px;
  }
  .contact__company {
    color: var(--orange);
    font-size: 28px;
    line-height: 38px;
    margin-bottom: 6px;
  }
  .contact__row {
    display: flex;
    align-items: center;
    gap: 10px;
    margin-top: 5px;
  }
  .icon {
    width: 26px; height: 26px;
    flex: none;
    background: var(--orange);
    border-radius: 4px;
    display: flex;
    align-items: center;
    justify-content: center;
  }
  .icon svg { width: 18px; height: 18px; }
  .contact__rule {
    height: 1px;
    background: var(--rule-grey);
    margin: 14px 0 12px;
  }
  .contact__person {
    color: var(--orange);
    font-size: 26px;
    line-height: 32px;
  }
  .contact__role { margin-bottom: 8px; }
</style>
</head>
<body>
<main class="canvas">

  <section class="card card--back" aria-label="Card back">
    <div class="brand"><span class="brand__name">Brisk</span></div>
    <p class="tagline">
      Specialising in design and production of training:<br>
      video | animation | illustration | text<br>
      for delivery via internet, intranet and/or LMS.
    </p>
  </section>

  <section class="card card--front" aria-label="Card front">
    <div class="brand"><span class="brand__name">Brisk</span></div>
    <div class="divider"></div>

    <div class="contact">
      <h1 class="contact__company">Brisk Lesson Studio</h1>
      <p>1st Floor, 418 Kellerby Road</p>
      <p>Mt Ferncombe, VIC 3862, Australia</p>

      <div class="contact__row">
        <span class="icon"><svg viewBox="0 0 24 24"><path fill="#1b1b1c" d="M6.6 10.8a15 15 0 0 0 6.6 6.6l2.2-2.2c.3-.3.7-.4 1-.2 1.1.4 2.3.6 3.6.6.6 0 1 .4 1 1V20c0 .6-.4 1-1 1A17 17 0 0 1 3 4c0-.6.4-1 1-1h3.5c.6 0 1 .4 1 1 0 1.3.2 2.5.6 3.6.1.3 0 .7-.2 1z"/></svg></span>
        <span>03 5172 4039</span>
      </div>
      <div class="contact__row">
        <span class="icon"><svg viewBox="0 0 24 24" fill="none" stroke="#1b1b1c" stroke-width="2"><circle cx="12" cy="12" r="9"/><path d="M3 12h18M12 3c3 3 3 15 0 18M12 3c-3 3-3 15 0 18"/></svg></span>
        <span>www.brisklesson.com.au</span>
      </div>

      <div class="contact__rule"></div>

      <h2 class="contact__person">Lionel Petch</h2>
      <p class="contact__role">Founder and Lead Consultant</p>

      <div class="contact__row">
        <span class="icon"><svg viewBox="0 0 24 24" fill="none" stroke="#1b1b1c" stroke-width="2"><rect x="7" y="2" width="10" height="20" rx="2"/><path d="M10 18h4"/></svg></span>
        <span>+61 3 0462 735 218</span>
      </div>
      <div class="contact__row">
        <span class="icon"><svg viewBox="0 0 24 24" fill="none" stroke="#1b1b1c" stroke-width="2"><rect x="3" y="5" width="18" height="14"/><path d="M3 5l9 8 9-8"/></svg></span>
        <span>lionel@brisklesson.com.au</span>
      </div>
    </div>
  </section>

</main>
</body>
</html>
```